Need to drive pregnant women to my 3d4d ultrasound studio where i provide 4d ultrasound with hyperalistic imaging and gender reveals

Industry/Entity Type

Healthcare

Font styles to use
Decorative
Script

Requirements
Must have
• My Company name Latido de Cielo Azul 4D. EVERYTHING HAS TO BE IN SPANISH
Nice to have
• SIMPLE AND NOT TOO BUSY
Should not have
• website

```html
<!DOCTYPE html>
<html lang="es">
<head>
<meta charset="utf-8">
<title>Latido de Cielo Azul 4D</title>
<link href="https://fonts.googleapis.com/css2?family=Exo+2:wght@800;900&family=Sora:wght@500;700&display=swap" rel="stylesheet">
<style>
  :root {
    --page: #eceef1;
    --peach: #f7dcc2;
    --navy: #14275f;
    --navy-light: #1f3a8a;
    --cream: #fbf4e6;
    --white: #ffffff;
  }
  html, body {
    margin: 0;
    width: 1200px;
    height: 900px;
    overflow: hidden;
    background: var(--page);
  }
  .billboard {
    position: absolute;
    left: 30px;
    top: 270px;
    width: 1140px;
    height: 360px;
    background: var(--peach);
    overflow: hidden;
    box-shadow: 0 10px 30px rgba(0,0,0,0.12);
  }
  .headline {
    position: absolute;
    left: 44px;
    top: 26px;
    margin: 0;
    font-family: "Exo 2", sans-serif;
    font-weight: 900;
    font-size: 84px;
    line-height: 0.86;
    letter-spacing: 1px;
    color: var(--navy);
    text-transform: uppercase;
  }
  .contact-band {
    position: absolute;
    left: 0;
    bottom: 0;
    width: 660px;
    height: 76px;
  }
  .contact-band svg { position: absolute; inset: 0; }
  .contact-text {
    position: absolute;
    left: 44px;
    top: 0;
    height: 76px;
    display: flex;
    align-items: center;
    gap: 18px;
    color: var(--white);
  }
  .contact-label {
    font-family: "Sora", sans-serif;
    font-weight: 500;
    font-size: 22px;
  }
  .contact-phone {
    display: flex;
    align-items: center;
    gap: 12px;
    font-family: "Sora", sans-serif;
    font-weight: 700;
    font-size: 40px;
    letter-spacing: 0.5px;
  }
  .heart {
    position: absolute;
  }
  .heart-scan { left: 620px; top: 52px; width: 300px; height: 280px; }
  .heart-newborn { left: 880px; top: 78px; width: 250px; height: 270px; }
</style>
</head>
<body>
  <section class="billboard">
    <h1 class="headline">Latido<br>de Cielo<br>Azul 4D</h1>

    <div class="contact-band">
      <svg viewBox="0 0 660 76" width="660" height="76" aria-hidden="true">
        <defs>
          <linearGradient id="bandFill" x1="0" y1="0" x2="1" y2="0">
            <stop offset="0" stop-color="var(--navy)"/>
            <stop offset="0.7" stop-color="var(--navy-light)"/>
            <stop offset="1" stop-color="var(--navy)"/>
          </linearGradient>
        </defs>
        <path d="M0 0 H600 Q612 0 618 10 L660 76 H0 Z" fill="url(#bandFill)"/>
      </svg>
      <div class="contact-text">
        <span class="contact-label">Para orientación</span>
        <span class="contact-phone">
          <svg width="22" height="30" viewBox="0 0 22 30" aria-hidden="true">
            <path d="M6 2 L10 9 L7 12 Q9 19 14 23 L17 20 L21 26 L17 29 Q8 27 3 16 Q0 8 2 4 Z" fill="none" stroke="var(--white)" stroke-width="2.4" stroke-linejoin="round"/>
          </svg>
          555-014-2378
        </span>
      </div>
    </div>

    <svg class="heart heart-scan" viewBox="0 0 100 92" role="img" aria-label="Imagen de ecografía 4D de un bebé en el vientre">
      <defs>
        <radialGradient id="scanFill" cx="0.55" cy="0.45" r="0.7">
          <stop offset="0" stop-color="#c9772c"/>
          <stop offset="0.6" stop-color="#9a4d16"/>
          <stop offset="1" stop-color="#5a2a0c"/>
        </radialGradient>
      </defs>
      <path d="M50 89 C20 66 2 46 2 27 C2 12 13 2 27 2 C38 2 46 9 50 19 C54 9 62 2 73 2 C87 2 98 12 98 27 C98 46 80 66 50 89 Z" fill="url(#scanFill)" stroke="var(--cream)" stroke-width="2.4"/>
    </svg>

    <svg class="heart heart-newborn" viewBox="0 0 100 108" role="img" aria-label="Fotografía de un recién nacido dormido">
      <defs>
        <radialGradient id="newbornFill" cx="0.45" cy="0.5" r="0.7">
          <stop offset="0" stop-color="#f6d2c0"/>
          <stop offset="0.7" stop-color="#eab7a0"/>
          <stop offset="1" stop-color="#d4957f"/>
        </radialGradient>
      </defs>
      <path d="M44 105 C18 86 2 62 2 34 C2 14 14 2 29 2 C40 2 48 10 52 22 C57 14 64 10 73 10 C88 10 98 22 98 38 C98 62 76 86 44 105 Z" fill="url(#newbornFill)" stroke="var(--cream)" stroke-width="2.4"/>
    </svg>
  </section>
</body>
</html>
```